Bramwell Quayle Lending Solutions business card design

Need a business card design for my mortgage broking business Bramwell Quayle Lending Solutions.

Target Market(s)

Mortgage clients/colleagues

Industry/Entity Type

Business

Requirements
Must have
• Must utilise logo attached. Possibly have logo only on back of card. my name & contact details on front and something creative?

Must incorporate purple/black/white in colour scheme.

Must incorporate tag line 'clear answers on every loan' under logo - using a script style fint. UPDATE: Mistral doesn't seem to be working on the card. Happy for you to try a different font. preferably a script style font.

Standard business card size.
Nice to have
• Try and incorporate the detective theme - but keep it looking sharp and professional.
Have attached some sample designs - does not have to be this - happy to review any ideas you may have.

```html
<!DOCTYPE html>
<html lang="en">
<head>
<meta charset="utf-8">
<title>Bramwell Quayle Lending Solutions – Business Card</title>
<link href="https://fonts.googleapis.com/css2?family=Open+Sans:wght@400;600&display=swap" rel="stylesheet">
<style>
  :root {
    --stage: #e9e6e2;
    --card-dark: #1b1b1e;
    --card-mid: #2e2e33;
    --purple: #4a2a8c;
    --plum: #5b1f5c;
    --band-dark: #141416;
    --band-slate: #2a2a38;
    --text-white: #f2f2f2;
    --text-grey: #b9b9bd;
  }
  * { box-sizing: border-box; margin: 0; padding: 0; }
  html, body { width: 1200px; height: 723px; overflow: hidden; }
  body {
    background: var(--stage);
    font-family: "Open Sans", Arial, sans-serif;
    display: flex;
    align-items: center;
    justify-content: center;
    gap: 40px;
  }
  .card {
    position: relative;
    width: 540px;
    height: 310px;
    border-radius: 4px;
    overflow: hidden;
    background: radial-gradient(ellipse at 40% 20%, var(--card-mid), var(--card-dark) 75%);
    box-shadow: 0 10px 28px rgba(0,0,0,0.28);
  }
  .card__bands {
    position: absolute;
    left: 0; top: 0;
    width: 100%; height: 100%;
  }
  /* Front */
  .front__details {
    position: absolute;
    left: 34px; top: 40px;
    color: var(--text-grey);
  }
  .front__name { font-size: 17px; font-weight: 600; color: var(--text-white); }
  .front__role { font-size: 12.5px; margin-top: 2px; }
  .front__contact { margin-top: 20px; font-size: 13px; line-height: 1.45; }
  .front__address {
    position: absolute;
    left: 34px; bottom: 22px;
    color: var(--text-white);
    font-size: 15px;
    line-height: 1.35;
  }
  /* Back */
  .brand {
    position: absolute;
    left: 60px; top: 60px;
    display: flex;
    align-items: center;
    gap: 12px;
  }
  .brand__dot {
    width: 22px; height: 22px;
    border-radius: 50%;
    background: var(--purple);
  }
  .brand__name {
    color: var(--purple);
    font-size: 30px;
    font-weight: 600;
    line-height: 1.05;
  }
  .brand__tagline {
    position: absolute;
    right: 44px; top: 136px;
    color: var(--text-grey);
    font-size: 16px;
    font-weight: 400;
    letter-spacing: 0.04em;
  }
</style>
</head>
<body>

<section class="card card--front" aria-label="Card front">
  <svg class="card__bands" viewBox="0 0 540 310" preserveAspectRatio="none" aria-hidden="true">
    <path d="M-20 175 Q270 130 560 185" fill="none" stroke="var(--band-slate)" stroke-width="16"/>
    <path d="M-20 205 Q270 160 560 215" fill="none" stroke="var(--plum)" stroke-width="14"/>
    <path d="M-20 232 Q270 190 560 243" fill="none" stroke="var(--band-dark)" stroke-width="14"/>
    <path d="M-20 258 Q270 218 560 270" fill="none" stroke="var(--plum)" stroke-width="12"/>
    <path d="M-20 290 Q270 250 560 300" fill="none" stroke="var(--plum)" stroke-width="10"/>
  </svg>
  <div class="front__details">
    <p class="front__name">Managing Director Clara Whitmore</p>
    <p class="front__role">Non-Conforming Mortgage Specialists</p>
    <p class="front__contact">Ph: 0412 555 019<br>e: clara@bramwellquayle.com.au</p>
  </div>
  <p class="front__address">Garnet House,<br>Level 1,<br>218 Ashby Lane<br>Melbourne 3000</p>
</section>

<section class="card card--back" aria-label="Card back">
  <svg class="card__bands" viewBox="0 0 540 310" preserveAspectRatio="none" aria-hidden="true">
    <path d="M-20 200 Q270 160 560 210" fill="none" stroke="var(--band-slate)" stroke-width="16"/>
    <path d="M-20 230 Q270 190 560 240" fill="none" stroke="var(--plum)" stroke-width="14"/>
    <path d="M-20 258 Q270 220 560 268" fill="none" stroke="var(--band-dark)" stroke-width="14"/>
    <path d="M-20 284 Q270 246 560 294" fill="none" stroke="var(--plum)" stroke-width="12"/>
  </svg>
  <div class="brand">
    <span class="brand__dot"></span>
    <p class="brand__name">Bramwell Quayle<br>Lending Solutions</p>
  </div>
  <p class="brand__tagline">clear answers on every loan</p>
</section>

</body>
</html>
```